Flyer design for commercial marketing

Looking to get a flyer design to email out to companies indicating our services
Company Name - Brightwell Networks
Company Logo - (Attached)
Services Offered
FULL HD DIGITAL IP CCTV SYSTEMS
IP ACCESS CONTROL SYSTEMS RFID / BIOMETRIC
IP EMPLOYEE MANAGEMENT SYSTEMS RFID / BIOMETRIC
NETWORKING / FIBER OPTIC SOLUTIONS
The designer can input necessary text and images
It is up to the designer to put images. I dont want the flyer too tacky. I am using this for commercial advertising
Updates
Target Market(s)
Corporate
Industry/Entity Type
It Company
Look and feel
Each slider illustrates characteristics of the customer's brand and the style your logo design should communicate.

```html
<!DOCTYPE html>
<html lang="en">
<head>
<meta charset="utf-8">
<title>Brightwell Networks – Services Flyer</title>
<link href="https://fonts.googleapis.com/css2?family=Open+Sans:wght@400;600;700&family=Roboto+Slab:wght@400;700&family=Oswald:wght@400;500&display=swap" rel="stylesheet">
<style>
  :root {
    --navy: #1c2a3a;
    --ink: #2a2c30;
    --band: #2c2e33;
    --accent: #3aa8e0;
    --accent-soft: #5cc0ee;
    --muted: #6a6d72;
    --paper: #ffffff;
    --rule: #b9bcc0;
  }
  * { margin: 0; padding: 0; box-sizing: border-box; }
  html, body { width: 859px; height: 1200px; overflow: hidden; background: var(--paper); }
  .flyer { position: relative; width: 859px; height: 1200px; background: var(--paper); font-family: "Open Sans", sans-serif; color: var(--ink); }

  .brand { position: absolute; left: 42px; top: 44px; display: flex; align-items: center; gap: 16px; }
  .brand-mark { width: 58px; height: 58px; border-radius: 50%; background: var(--navy); }
  .brand-name { font-family: "Roboto Slab", serif; font-weight: 700; color: var(--navy); font-size: 30px; line-height: 1.05; letter-spacing: 1px; text-transform: uppercase; }
  .brand-name small { display: block; font-size: 17px; letter-spacing: 2px; }

  .contact { position: absolute; left: 565px; top: 56px; font-size: 11px; line-height: 1.6; color: var(--muted); }

  .hero { position: absolute; left: 0; top: 138px; width: 859px; height: 342px;
    background: radial-gradient(ellipse at 75% 45%, #9fd8f5 0%, #3d8fc8 30%, #15406e 65%, #0b2444 100%); }
  .hero-lines { position: absolute; left: 42px; top: 66px; }
  .hero-lines span { display: table; background: rgba(20,28,40,0.78); color: #fff; font-size: 38px; line-height: 1.15; padding: 2px 12px 4px; margin-bottom: 2px; }
  .hero-lines em { font-style: normal; color: var(--accent-soft); }
  .hero-sub { position: absolute; left: 54px; top: 214px; width: 330px; font-size: 11px; line-height: 1.7; color: #e6f1f8; }

  .band { position: absolute; left: 0; top: 480px; width: 859px; height: 228px; background: var(--band); }
  .band-title { position: absolute; left: 42px; top: 44px; font-family: "Roboto Slab", serif; font-weight: 700; font-size: 46px; line-height: 1.15; color: #fff; }
  .band-title em { font-style: normal; color: var(--accent); }
  .band-copy { position: absolute; left: 430px; top: 46px; width: 390px; font-size: 11.5px; line-height: 1.65; color: #e4e5e7; }

  .services { position: absolute; left: 0; top: 722px; width: 859px; height: 440px; }
  .services::after { content: ""; position: absolute; left: 429px; top: 10px; height: 420px; border-left: 2px dotted var(--rule); }
  .service { position: absolute; width: 360px; text-align: center; }
  .service h3 { font-family: "Oswald", sans-serif; font-weight: 400; font-size: 26px; line-height: 1.1; color: var(--ink); text-transform: uppercase; }
  .service h3 strong { display: block; font-weight: 500; font-size: 28px; }
  .service p { margin: 16px auto 0; width: 300px; text-align: left; font-size: 11.5px; line-height: 1.6; color: var(--muted); }
  .service::after { content: ""; display: block; margin: 26px auto 0; width: 330px; border-top: 2px dashed var(--rule); }
  .s1 { left: 42px; top: 10px; } .s2 { left: 460px; top: 10px; }
  .s3 { left: 42px; top: 218px; } .s4 { left: 460px; top: 218px; }

  .footer-strip { position: absolute; left: 0; bottom: 0; width: 859px; height: 20px; background: var(--accent-soft); }
</style>
</head>
<body>
<main class="flyer">
  <header>
    <div class="brand">
      <span class="brand-mark"></span>
      <div class="brand-name">Brightwell<small>Networks</small></div>
    </div>
    <address class="contact" style="font-style:normal">
      88 Harbour Lane, Leeds<br>
      Phone : +00 4410 2285 | Fax : 987 654 321<br>
      Email : hello@brightwellnet.com
    </address>
  </header>

  <section class="hero" role="img" aria-label="Glowing blue world map crossed by bright network connection lines">
    <div class="hero-lines">
      <span>Hello, we help you</span>
      <span>turn your <em>ideas</em></span>
      <span>into reality</span>
    </div>
    <p class="hero-sub">Take the right decisions for your business and develop it with your creative idea and creative concept.</p>
  </section>

  <section class="band">
    <h2 class="band-title">How to<br>be <em>effective?</em></h2>
    <p class="band-copy">Lorem ipsum dolor sit amet consectetur adipiscing elit, sed do eiusmod tempor incididunt ut labore et dolore magna aliqua dolore eu consectetur adipisicing elit sed do eiusmod tempor incididunt ut labore et dolore adipiscing of tempor incididunt magna et dolore sit ut dolor sit amet.</p>
  </section>

  <section class="services">
    <article class="service s1">
      <h3>Full HD Digital<strong>IP CCTV Systems</strong></h3>
      <p>Lorem ipsum dolor sit adipiscing elit, sed do eiusmod tempor incididunt ut labore et dolore magna aliqua sit amet consectetur.</p>
    </article>
    <article class="service s2">
      <h3>IP Access Control<strong>Systems RFID / Biometric</strong></h3>
      <p>Lorem ipsum dolor sit adipiscing elit, sed do eiusmod tempor incididunt ut labore et dolore magna aliqua sit amet consectetur.</p>
    </article>
    <article class="service s3">
      <h3>IP Employee Management<strong>Systems RFID / Biometric</strong></h3>
      <p>Lorem ipsum dolor sit adipiscing elit, sed do eiusmod tempor incididunt ut labore et dolore magna aliqua sit amet consectetur.</p>
    </article>
    <article class="service s4">
      <h3>Networking / Fiber<strong>Optic Solutions</strong></h3>
      <p>Lorem ipsum dolor sit adipiscing elit, sed do eiusmod tempor incididunt ut labore et dolore magna aliqua sit amet consectetur.</p>
    </article>
  </section>

  <div class="footer-strip"></div>
</main>
</body>
</html>
```